Brochure Design Project

I need a brochure design for a full Hair Salon, located in Rockville MD called Coralind Hair, Nails and Spa.
Please use inovative design (the idea is to target an audience between the age of 19 to 50) keeping our main colors (spring green, grey and white).
we would also like to include the list of services which will be provided when needed.

Target Market(s)

women between 19 to 50 - all ethnical backgrounds

Industry/Entity Type

Hair

Requirements
Nice to have
• we would like to include a blurb, contact info and list of prices of all the services we provided. Also we would like to add the line "se habla espaƱol" anywhere in the brochure.

```html
<!DOCTYPE html>
<html lang="en">
<head>
<meta charset="utf-8">
<title>Coralind Hair, Nails and Spa – Brochure</title>
<link rel="stylesheet" href="https://fonts.googleapis.com/css2?family=Questrial&family=Tinos:wght@700&display=swap">
<style>
  :root {
    --spring: #c7da7f;
    --spring-bright: #b8d05e;
    --grey-dark: #59595b;
    --grey-mid: #949597;
    --white: #ffffff;
    --ink: #1e1e1e;
    --hair-deep: #2a1712;
    --hair-warm: #7a2e1e;
    --skin: #d9a488;
  }
  html, body {
    margin: 0;
    padding: 0;
    overflow: hidden;
    background: var(--white);
  }
  .brochure {
    position: relative;
    width: 1200px;
    height: 935px;
    overflow: hidden;
    background: var(--white);
    font-family: "Questrial", "Century Gothic", sans-serif;
  }
  .panel-about {
    position: absolute;
    left: 19px; top: 19px;
    width: 386px; height: 893px;
    background: linear-gradient(to bottom, var(--spring) 0%, var(--spring) 66%, var(--white) 74%);
  }
  .about-heading {
    position: absolute;
    left: 42px; top: 51px;
    width: 305px; height: 41px;
    margin: 0;
    background: linear-gradient(to bottom, #f4f4f4 0%, #c9c9c9 55%, #8e8e8e 100%);
    box-shadow: 0 3px 4px rgba(0,0,0,0.25);
    font-weight: 400;
    font-size: 21px;
    line-height: 41px;
    text-align: center;
    color: var(--ink);
  }
  .about-copy {
    position: absolute;
    left: 14px; top: 127px;
    width: 358px;
    text-align: center;
    font-size: 17px;
    line-height: 17.6px;
    color: var(--ink);
  }
  .about-copy p { margin: 0 0 17px; }
  .photo-model-bob {
    position: absolute;
    left: 19px; top: 609px;
    width: 386px; height: 303px;
    background: radial-gradient(ellipse at 42% 55%, rgba(217,164,136,0.85) 0%, rgba(217,164,136,0.5) 30%, rgba(40,30,25,0.9) 55%, rgba(40,30,25,0) 80%);
  }
  .photo-hero {
    position: absolute;
    left: 405px; top: 19px;
    width: 773px; height: 585px;
    background:
      radial-gradient(ellipse at 70% 45%, var(--skin) 0%, rgba(217,164,136,0.6) 22%, rgba(42,23,18,0) 45%),
      linear-gradient(150deg, var(--hair-warm) 0%, var(--hair-deep) 45%, #4a2219 75%, #1c100c 100%);
  }
  .hero-tagline {
    position: absolute;
    left: 451px; top: 104px;
    width: 310px;
    margin: 0;
    font-size: 13px;
    line-height: 15.5px;
    color: rgba(255,255,255,0.85);
  }
  .shapes {
    position: absolute;
    left: 0; top: 0;
  }
  .contact-block {
    position: absolute;
    left: 548px; top: 560px;
    transform: rotate(40deg);
    transform-origin: left top;
    color: var(--white);
    white-space: nowrap;
  }
  .contact-brand {
    margin: 0 0 0 18px;
    font-size: 40px;
    line-height: 44px;
    color: var(--spring-bright);
  }
  .contact-brand-sub {
    margin: 0 0 6px 98px;
    font-family: "Tinos", "Times New Roman", serif;
    font-weight: 700;
    font-size: 10px;
    letter-spacing: 0.5px;
  }
  .contact-lines {
    margin: 0;
    font-style: normal;
    font-size: 14.5px;
    line-height: 21px;
  }
  .contact-lines span { display: block; }
  .brand-mark {
    position: absolute;
    left: 834px; top: 680px;
    margin: 0;
    font-size: 62px;
    line-height: 70px;
    font-weight: 400;
    color: var(--spring-bright);
  }
  .brand-descriptor {
    position: absolute;
    left: 998px; top: 758px;
    margin: 0;
    font-family: "Tinos", "Times New Roman", serif;
    font-weight: 700;
    font-size: 13px;
    letter-spacing: 0.4px;
    color: var(--white);
  }
  .spanish-note {
    position: absolute;
    left: 814px; top: 829px;
    width: 364px; height: 41px;
    margin: 0;
    padding-left: 14px;
    box-sizing: border-box;
    background: var(--spring);
    box-shadow: -3px 3px 4px rgba(0,0,0,0.3);
    font-size: 26px;
    line-height: 41px;
    color: var(--ink);
  }
</style>
</head>
<body>
<main class="brochure">
  <section class="panel-about">
    <h2 class="about-heading">About Us</h2>
    <div class="about-copy">
      <p>Coralind Hair, Nails and Spa was founded by Lucinda Varela and Marisol Varela. Aside from being a mother and daughter, they are both professionals with the vision of providing the Washington metropolitan area, beauty services of the highest quality within a cheerful, relaxing, and friendly environment.</p>
      <p>Lucinda Varela, originally from Colombia, South America, is an experienced beauty professional passionate about her work, with over 25 years of experience in the beauty industry.</p>
      <p>Our international staff has a long history of providing excellent customer service, and will help to find the look that's right for you. When you visit, you will feel as if you were at home.</p>
    </div>
  </section>

  <div class="photo-model-bob" role="img" aria-label="Photo of a model with a sleek dark bob haircut"></div>

  <div class="photo-hero" role="img" aria-label="Photo of a woman with long flowing auburn hair"></div>
  <p class="hero-tagline">We specialize in providing a pleasant experience for all the family members in need of full service beauty salon with very affordable prices.</p>

  <svg class="shapes" width="1200" height="935" viewBox="0 0 1200 935" aria-hidden="true">
    <polygon class="shape-contact-panel" points="405,612 639,436 797,621 797,912 405,912" fill="var(--grey-dark)"/>
    <polygon class="shape-accent-strip" points="762,604 1178,604 1178,627 787,627" fill="var(--spring)"/>
    <rect class="shape-cover-panel" x="791" y="627" width="387" height="285" fill="var(--grey-mid)"/>
  </svg>

  <div class="contact-block">
    <p class="contact-brand">Coralind</p>
    <p class="contact-brand-sub">HAIR, NAILS &amp; SPA</p>
    <address class="contact-lines">
      <span>4810 Alder Grove Lane, Rockville,</span>
      <span>Maryland 20850</span>
      <span>+1 301-555-0142</span>
      <span>lucinda@coralindsalon.com</span>
      <span>www.coralindhns.com</span>
    </address>
  </div>

  <h1 class="brand-mark">Coralind</h1>
  <p class="brand-descriptor">HAIR, NAILS &amp; SPA</p>
  <p class="spanish-note">se habla español</p>
</main>
</body>
</html>
```